Menu Design solstane

I need to create a take out menu for my restaurant something nice with some pictures. clean and simple with the colors of my reatsurant. which are orange and black. mostly black.

its fairly simple it has to be 4 pages front cover, inside front menu then 2nd page front and back with menu then 3rd page back front menu, back 3rd sushi menu with specials. final page 4th page, back map with adress and opening hours. and back cover final.

simple elegant and class. black and orange i will send logo and menu as well and pictures.

i am a high end bistro that serves gourmet pizza and pasta. we also have a sushi bar.
the menu will be 6 inches width by 9 inches

the menu that i sent is a pdf file. had an error with word please change font and make a new word dosument.

thank you

• the colors which are black and orange. mostly black.

```html
<!DOCTYPE html>
<html lang="fr">
<head>
<meta charset="utf-8">
<title>Solstane – Menu</title>
<link rel="stylesheet" href="https://fonts.googleapis.com/css2?family=Righteous&family=Oswald:wght@400&display=swap">
<style>
  :root {
    --orange: #f0961e;
    --ink: #1e1e1e;
    --panel: rgba(38, 38, 38, 0.86);
    --strip: rgba(150, 150, 150, 0.28);
    --page-bg: #ffffff;
    --photo-light: #a6a6a6;
    --photo-mid: #6e6e6e;
    --photo-dark: #2e2e2e;
    --logo: rgba(20, 20, 20, 0.75);
  }
  * { margin: 0; padding: 0; box-sizing: border-box; }
  html, body { width: 1200px; height: 900px; overflow: hidden; background: var(--page-bg); }
  .canvas { position: relative; width: 1200px; height: 900px; }
  .spread {
    position: absolute; left: 75px; top: 57px; width: 1053px; height: 788px;
    overflow: hidden; box-shadow: 0 18px 22px -14px rgba(0,0,0,0.45);
  }
  .photo-backdrop {
    position: absolute; inset: 0;
    background:
      radial-gradient(ellipse at 35% 30%, var(--photo-light) 0%, rgba(0,0,0,0) 55%),
      linear-gradient(160deg, var(--photo-mid) 0%, var(--photo-dark) 70%, #1c1c1c 100%);
  }
  .center-strip { position: absolute; left: 458px; top: 0; width: 122px; height: 788px; background: var(--strip); }
  .column { position: absolute; top: 0; width: 418px; height: 788px; font-family: "Righteous", sans-serif; color: var(--orange); }
  .column--left { left: 40px; }
  .column--right { left: 580px; }
  .panel { position: absolute; left: 0; width: 418px; background: var(--panel); }
  .section-bar {
    position: absolute; left: 0; width: 418px; height: 32px; background: var(--orange);
    color: var(--ink); font-size: 16px; text-align: center; line-height: 33px; letter-spacing: 0.3px;
  }
  .section-note { position: absolute; left: 0; width: 418px; text-align: center; font-size: 16px; letter-spacing: 0.4px; }
  .line { position: absolute; left: 17px; font-size: 9.5px; line-height: 12px; text-transform: uppercase; white-space: nowrap; letter-spacing: 0.1px; }
  .price { position: absolute; right: 25px; font-size: 9.5px; line-height: 12px; }
  .drink-list { position: absolute; list-style: none; font-size: 9.5px; text-transform: uppercase; }
  .drink-list li { display: flex; justify-content: space-between; height: 13.4px; line-height: 13.4px; white-space: nowrap; }
  .brand-mark {
    position: absolute; bottom: 12px; font-family: "Righteous", sans-serif; font-size: 44px;
    color: var(--logo); letter-spacing: 1px;
  }
  .brand-mark--left { left: -8px; }
  .brand-mark--right { left: 905px; }
</style>
</head>
<body>
<div class="canvas">
  <div class="spread">
    <div class="photo-backdrop" role="img" aria-label="Black and white photograph of the bistro dining room with tables, chairs and a counter"></div>
    <div class="center-strip"></div>

    <section class="column column--left">
      <div class="panel" style="top:0;height:788px;"></div>
      <h2 class="section-bar" style="top:0;">ENTREES / APPETIZERS</h2>

      <p class="line" style="top:51px;">BRUSCHETTA (6)</p><span class="price" style="top:51px;">$8.50</span>
      <p class="line" style="top:64px;">TOMATOES, BASILIC, OIGNONS, HUILE D'OLIVE</p>
      <p class="line" style="top:77px;">TOMATOES, BASIL, ONIONS, OLIVE OIL &amp; GARLIC</p>

      <p class="line" style="top:104px;">BRUSCHETTA AU TARTARE DE SAUMON (4)</p><span class="price" style="top:104px;">$10.25</span>
      <p class="line" style="top:117px;">TARTARE DE SAUMON, TOMATES, BASILIC, OIGNONS, HUILE D'OLIVE &amp; AIL</p>
      <p class="line" style="top:130px;">SALMON TARTAR, TOMATOES, BASIL, ONIONS, OLIVE OIL &amp; GARLIC</p>

      <p class="line" style="top:156px;">PAIN GRATINE / CHEESE BREAD</p><span class="price" style="top:156px;">$7.50</span>
      <p class="line" style="top:183px;">RONDELLE D'OIGNION / ONION RING</p><span class="price" style="top:183px;">$4.50</span>
      <p class="line" style="top:209px;">SOUPE DU JOUR / SOUP OF THE DAY</p><span class="price" style="top:209px;">$3.95</span>
      <p class="line" style="top:235px;">SOUPE A L'OIGNON GRATINEE / ONION SOUP</p><span class="price" style="top:235px;">$6.95</span>
      <p class="line" style="top:262px;">CREVETTES A L'AIL / GARLIC SHRIMP (6) PIECES</p><span class="price" style="top:262px;">$8.95</span>

      <h2 class="section-bar" style="top:288px;">SALADES REPAS</h2>

      <p class="line" style="top:335px;">SALADE CEASAR / CEASAR SALAD</p><span class="price" style="top:335px;">$12.95</span>
      <p class="line" style="top:348px;">LAITUES, CROUTONS, PARMESAN &amp; VINAIGRETTE CAESAR MAISON</p>
      <p class="line" style="top:361px;">LETTUCE, CROUTONS, PARMESAN &amp; HOUSE CAESAR DRESSING MADE WITH</p>
      <p class="line" style="top:374px;">ANCHOVIES &amp; CAPERS</p>

      <p class="line" style="top:401px;">SALADE NICOISE / NICOISE SALAD</p><span class="price" style="top:401px;">$15.95</span>
      <p class="line" style="top:414px;">HARICOTS, POMME DE TERRE, THON, TOMATES, CONCOMBRE, OEUFS &amp;</p>
      <p class="line" style="top:427px;">VINAIGRETTE MAISON</p>
      <p class="line" style="top:440px;">GREEN BEANS, POTATOES, TUNA, TOMATOES, CUCUMBERS, EGGS HOUSE VINAIGRETTE</p>

      <p class="line" style="top:466px;">SALADE FROMAGE DE CHEVRE / GOAT CHEESE SALAD</p><span class="price" style="top:466px;">$15.95</span>
      <p class="line" style="top:479px;">LAITUES, , PIMENTS, FROMAGE DE CHEVRES , TOMATE, CONCOMBRE</p>
      <p class="line" style="top:492px;">LETTUCE, , PEPPERS, GOAT CHEESE, TOMATO, CUCUMBERS</p>

      <p class="line" style="top:519px;">SALADE FRUIT DE MER / SEAFOOD SALAD</p><span class="price" style="top:519px;">$15.95</span>
      <p class="line" style="top:532px;">LAITUE, GOBERGE, PIMENTS, MAYONNAISE &amp; MORCEAUX D'ORANGE</p>
      <p class="line" style="top:545px;">LETTUCE, PEPPERS, PEPPERS CRAB STICKS &amp; ORANGE PIECES</p>

      <p class="line" style="top:586px;">SALADE GRECQUE / GREEK SALAD</p><span class="price" style="top:586px;">$15.95</span>
      <p class="line" style="top:599px;">TOMATES, CONCOMBRES, OGNION ROUGE, OLIVES KALAMATA, FROMAGE FETA</p>
      <p class="line" style="top:612px;">TOMATOES, CUCUMBERS, RED ONIONS, RED PEPPERS, OLIVES, FETA</p>

      <p class="line" style="top:638px;">SALADE DE SAUMON FUME CAPRES &amp; OGNIONS</p><span class="price" style="top:638px;">$12.95</span>
    </section>

    <section class="column column--right">
      <div class="panel" style="top:0;height:788px;"></div>
      <h2 class="section-bar" style="top:0;">PETIT DEJEUNER / BREAKFAST</h2>
      <p class="section-note" style="top:35px;">SERVI JUSQU'A 3HRS / SERVED UNTIL 3PM</p>

      <p class="line" style="top:67px;">DEUX OEUFS / TWO EGGS</p><span class="price" style="top:67px;">$9.50</span>
      <p class="line" style="top:80px;">OEUFS BROUILLES / SCRAMBLED EGGS (3)</p>
      <p class="line" style="top:107px;">OEUFS BROUILLES NATURE / PLAIN SCRAMBLED EGGS</p><span class="price" style="top:107px;">$10.00</span>
      <p class="line" style="top:133px;">OEUFS BROUILLES &amp; ASPERGES</p><span class="price" style="top:133px;">$10.50</span>
      <p class="line" style="top:159px;">OEUFS BROUILLES AU SAUMON FUME</p><span class="price" style="top:159px;">$12.95</span>
      <p class="line" style="top:185px;">OEUFS BROUILLES AUX CHAMPIGNONS</p><span class="price" style="top:185px;">$10.50</span>
      <p class="line" style="top:212px;">OMELETTE (3)</p><span class="price" style="top:212px;">$10.00</span>
      <p class="line" style="top:225px;">OMELETTE NATURE / PLAIN OMELET</p>
      <p class="line" style="top:252px;">OMELETTE ESPAGNOLE / SPANISH OMELET</p><span class="price" style="top:252px;">$10.50</span>
      <p class="line" style="top:278px;">OMELETTE AUX OLIVES / OLIVE OMELET</p><span class="price" style="top:278px;">$10.50</span>
      <p class="line" style="top:304px;">OMELETTE AUX FINES HERBES / FINE HERB OMELET</p><span class="price" style="top:304px;">$10.50</span>
      <p class="line" style="top:330px;">OMELETTE AU FROMAGE / CHEESE OMELET</p><span class="price" style="top:330px;">$10.50</span>
      <p class="line" style="top:357px;">OMELETTE AUX CHAMPIGNONS / MUSHROOM OMELET</p><span class="price" style="top:357px;">$10.50</span>
      <p class="line" style="top:383px;">OMELETTE AU SAUMON FUME / SMOKED SALMON OMELET</p><span class="price" style="top:383px;">$12.95</span>
      <p class="line" style="top:409px;">SALADE DE FRUIT FRAIS</p><span class="price" style="top:409px;">$4.50</span>

      <div class="section-bar" style="top:435px;"></div>
      <h2 class="section-bar" style="top:435px;width:210px;background:none;">BOISSON CHAUDES</h2>
      <h2 class="section-bar" style="top:435px;left:205px;width:210px;background:none;">BOISSONS FROIDES</h2>

      <ul class="drink-list" style="left:17px;top:474px;width:142px;">
        <li><span>CAFE FILTRE</span><span>$2.00</span></li>
        <li><span>EXPRESSO ALLONGE</span><span>$2.75</span></li>
        <li><span>DOUBLE EXPRESSO</span><span>$3.00</span></li>
        <li><span>MACCHIATO</span><span>$2.75</span></li>
        <li><span>MACCHIATO DOUBLE</span><span>$3.25</span></li>
        <li><span>CAPPUCCINO</span><span>$3.25</span></li>
        <li><span>CAPPUCCINO BOL</span><span>$3.75</span></li>
        <li><span>CAFE MOCHA</span><span>$3.75</span></li>
        <li><span>CHOCOLAT CHAUD</span><span>$3.75</span></li>
        <li><span>CAFE LATT</span><span>$3.25</span></li>
      </ul>
      <ul class="drink-list" style="left:213px;top:474px;width:180px;">
        <li><span>NON-FAT ICED CAP</span><span>$4.95</span></li>
        <li><span>ICED CAPPUCCINO</span><span>$4.95</span></li>
        <li><span>ICED MOCHA</span><span>$4.95</span></li>
        <li><span>CHOCOLAT FROID</span><span>$3.25</span></li>
        <li><span>ICE COFFEE</span><span>$3.95</span></li>
        <li><span>SMOOTHIES AUX FRUITS</span><span>$4.25</span></li>
        <li><span>SELECTION DU JOURCAPPUCCINO BOL</span><span>$3.75</span></li>
        <li><span>CAFE MOCHA</span><span>$3.75</span></li>
        <li><span>JUS D'ORANGE</span><span>$3.95</span></li>
        <li><span>JUS DE POMME</span><span>$3.50</span></li>
      </ul>
    </section>

    <p class="brand-mark brand-mark--left">solstane</p>
    <p class="brand-mark brand-mark--right">solstane</p>
  </div>
</div>
</body>
</html>
```